Brume d'Orvelle Hand Crafted Candles promotional flyer

Hand Crafted Soy Candles - I need a flyer to promote my candles and to give information on care of candles.I want this to use the design and colours I already have for my labels and the photo I have attached.I am aiming at a sophisticated market so would like to reflect this in the design.
Should appeal to sophisticated women who enjoy the pleasure of candles - to enhance their enjoyment of life - gives them the 'brume d'orvelle'.
the candles are hand crafted from all natural ingredients, environmentally friendly and with exquisite fragrances

Target Market(s)

sophisticated females

Industry/Entity Type

Promotional

Font styles to use
Script

Colors
cfeae6
ecdaeb

Requirements
Must have
• something expressing 'brume d'orvelle' - the enjoyment of candles
Should not have
• bright colours

```html
<!DOCTYPE html>
<html lang="en">
<head>
<meta charset="utf-8">
<title>Brume d'Orvelle Hand Crafted Candles</title>
<link href="https://fonts.googleapis.com/css2?family=Great+Vibes&family=Italianno&family=Parisienne&display=swap" rel="stylesheet">
<style>
  :root {
    --mint: #cfeae6;
    --mint-deep: #9fd6cc;
    --blush: #ecdaeb;
    --charcoal: #2f2e2b;
    --charcoal-dark: #1f1e1c;
    --ink: #3a3a3a;
    --text-light: #e6dde4;
    --paper: #ffffff;
  }
  * { margin: 0; padding: 0; box-sizing: border-box; }
  html, body { width: 850px; height: 1200px; overflow: hidden; background: var(--paper); }
  .flyer { position: relative; width: 850px; height: 1200px; overflow: hidden; background: var(--paper); }
  .backdrop { position: absolute; inset: 0; }
  .title-band { position: absolute; left: 150px; top: 38px; width: 550px; height: 58px;
    background: linear-gradient(180deg, #4a4a47, #2c2b29); border-radius: 50% / 18px;
    display: flex; align-items: center; justify-content: center; }
  .title-band h1 { font-family: "Great Vibes", cursive; font-weight: 400; font-size: 44px; color: var(--paper); letter-spacing: 1px; }
  .flourish { position: absolute; top: 44px; width: 70px; height: 40px; background: linear-gradient(90deg, #9a9a98, #4a4a47); border-radius: 20px; opacity: .55; }
  .flourish.left { left: 100px; }
  .flourish.right { right: 100px; transform: scaleX(-1); }
  .hero-photo { position: absolute; left: 72px; top: 116px; width: 228px; height: 238px;
    background: radial-gradient(ellipse at 50% 48%, #dfe7ea 0 38%, #1d1d22 40% 100%); border-radius: 10px 10px 16px 16px; }
  .features { position: absolute; left: 382px; top: 138px; width: 370px; list-style: none;
    font-family: "Italianno", cursive; font-size: 29px; line-height: 23px; color: var(--ink); }
  .features li { position: relative; padding-left: 22px; margin-bottom: 8px; }
  .features li::before { content: ""; position: absolute; left: 2px; top: 9px; width: 7px; height: 7px; border-radius: 50%; background: #7a7a7a; }
  .heading { font-family: "Great Vibes", cursive; font-weight: 400; color: var(--blush); border-bottom: 1px solid #8e8a8c; }
  .info { list-style: none; font-family: "Parisienne", cursive; font-size: 10.5px; line-height: 13px; color: var(--text-light); }
  .info li { position: relative; padding-left: 18px; margin-bottom: 9px; }
  .info li::before { content: ""; position: absolute; left: 2px; top: 3px; width: 6px; height: 6px; border-radius: 50%; background: #a49ea2; }
  .col-left { position: absolute; left: 72px; top: 556px; width: 276px; }
  .col-left .heading { font-size: 24px; padding: 0 0 2px 22px; margin-bottom: 12px; }
  .col-left .heading.refill { margin-top: 18px; font-size: 26px; }
  .contact { position: absolute; left: 72px; top: 930px; width: 240px; border-top: 3px double #8e8a8c; padding: 14px 0 0 2px;
    font-family: "Italianno", cursive; font-size: 21px; line-height: 17px; color: var(--text-light); }
  .contact .lines { margin-top: 12px; font-size: 23px; line-height: 18px; }
  .col-right { position: absolute; left: 436px; top: 558px; width: 348px; }
  .col-right .heading { font-size: 19px; line-height: 17px; text-align: center; padding-bottom: 6px; margin-bottom: 12px; }
  .col-right .info li { margin-bottom: 10px; }
  .rule-bottom { position: absolute; left: 72px; top: 1052px; width: 710px; border-top: 1px solid #8e8a8c; }
  .brand-mark { position: absolute; left: 72px; top: 1056px; width: 104px; height: 104px; border-radius: 50%; background: var(--mint);
    border: 2px solid var(--paper); display: flex; align-items: center; justify-content: center; text-align: center;
    font-family: "Italianno", cursive; font-size: 19px; line-height: 16px; color: var(--ink); }
  .product-row { position: absolute; left: 272px; top: 1076px; width: 324px; height: 68px;
    background: linear-gradient(90deg, #2b3d8a 0 6%, #e9e7df 10% 34%, #1a1a1d 38% 62%, #e9e7df 66% 90%, #2b3d8a 94%); border-radius: 4px; opacity: .9; }
</style>
</head>
<body>
<main class="flyer">
  <svg class="backdrop" width="850" height="1200" viewBox="0 0 850 1200" aria-hidden="true">
    <defs>
      <radialGradient id="slate" cx="50%" cy="40%" r="75%">
        <stop offset="0" stop-color="#3b3a37"/>
        <stop offset="1" stop-color="#1f1e1c"/>
      </radialGradient>
      <linearGradient id="mintFade" x1="0" y1="0" x2="1" y2="0">
        <stop offset="0" stop-color="#cfeae6" stop-opacity=".3"/>
        <stop offset=".6" stop-color="#9fd6cc"/>
        <stop offset="1" stop-color="#cfeae6" stop-opacity=".7"/>
      </linearGradient>
    </defs>
    <path d="M560 0 C700 60 850 90 850 200 L850 540 C700 500 560 420 420 360 C260 290 120 330 0 360 L0 300 C140 250 300 230 420 280 C560 330 700 300 760 220 C820 140 700 60 560 0 Z" fill="#cfeae6" opacity=".55"/>
    <path d="M120 360 C260 300 420 330 540 400 C660 470 760 470 850 440 L850 470 C740 520 620 500 500 440 C380 380 240 370 120 360 Z" fill="url(#mintFade)"/>
    <path d="M0 470 C120 430 240 440 320 470 C420 510 560 500 680 440 C760 400 820 420 850 430 L850 1200 L0 1200 Z" fill="#cfeae6" opacity=".6"/>
    <path d="M0 480 C140 440 260 470 360 440 C480 400 600 470 720 440 C790 420 830 440 850 446 L850 1200 L0 1200 Z" fill="url(#slate)"/>
    <ellipse cx="434" cy="1185" rx="310" ry="45" fill="#171615"/>
  </svg>

  <div class="flourish left" role="img" aria-label="Decorative scroll ornament"></div>
  <div class="flourish right" role="img" aria-label="Decorative scroll ornament"></div>
  <header class="title-band"><h1>Brume d'Orvelle</h1></header>

  <div class="hero-photo" role="img" aria-label="Photo of a black glass candle jar with a pale round label"></div>

  <ul class="features">
    <li>Brume d'Orvelle - an exuberant enjoyment of life - these candles will fill you with "Brume d'Orvelle"</li>
    <li>Candles are lovingly hand-poured and use only the finest of ingredients and fragrances</li>
    <li>Hand crafted soy candle creations</li>
    <li>Completely non-toxic</li>
    <li>Exquisite fragrances</li>
    <li>Clean burning</li>
    <li>Environmentally friendly</li>
  </ul>

  <section class="col-left">
    <h2 class="heading">Why soy wax?</h2>
    <ul class="info">
      <li>Soft smooth wax that burns clear - no soot or smoke</li>
      <li>Soy wax candles burn up to 50% longer than traditional paraffin candles</li>
      <li>Made form soya beans, a renewable natural resource that supports and sustains agriculture - it is biodegradable and environmentally friendly</li>
      <li>Soy wax burns cooler than paraffin and disperse the fragrance more fully</li>
    </ul>
    <h2 class="heading refill">Containers can be refilled</h2>
    <ul class="info">
      <li>I offer a refill service - if you return you containers to me I can refill with the fragrance of your choice</li>
      <li>Or if you have a special container you would like to use for your candle just contact me for a quote</li>
    </ul>
  </section>

  <section class="contact">
    <p>I have a wide range of fragrances<br>- please contact me for details:</p>
    <p class="lines">Email: celine.marrow@mailbox.nz<br>Mobile: 021 555 0148<br>Website: www.brumedorvelle.co.nz</p>
  </section>

  <section class="col-right">
    <h2 class="heading">How to care for your candle - the following tips will ensure you have a long lasting, fully fragranced candle</h2>
    <ul class="info">
      <li>When lighting you candle for the first time, allow the wax to melt all the way to the sides of the container - this creates a 'memory' and avoids 'tunnelling' as the candle burns</li>
      <li>Always trim the wick to about 6-8mm before re-lighting your candle. This will ensure a long lasting candle, minimise soot and remove any mushrooming of the wick from a previous burn</li>
      <li>It is preferable to use a candle 'snuffer' to extinguish the flame, or a lid if the candle has one. Alternatively, you can dip the wick into the melted wax and then straightening. This wil stop the wick from smoking and help with relighting</li>
      <li>All Brume d'Orvelle candles are hand poured not massed produced - although every effort is made to ensure consistency, every candle may be different</li>
      <li>Sometimes you may notice darker patches or wet spots - this is not a fault it is just he natural way the wax has set - it does not affect the candle in anyway</li>
      <li>The top of the candle may also appear slightly uneven - this is just a sign of natural soy wax being hand poured</li>
      <li>Do not leave your candle in the sunlight as it may turn a yellow colour - again this does not affect the candle in anyway - it just loses its creamy white colour</li>
      <li>As these candles contain no preservatives or chemicals it is recommended that they should be used within 6 months</li>
    </ul>
  </section>

  <div class="rule-bottom"></div>
  <div class="brand-mark">Brume d'Orvelle<br>Hand Crafted Candles</div>
  <div class="product-row" role="img" aria-label="Photo of a row of candles in blue, clear and black glass jars"></div>
</main>
</body>
</html>
```